you will use Ai to Copy the website Quellabyx.com to come up with the basic frame work and it will give you the understanding of how I would like Zandoprik.com to be like. Zandoprik.com is a peer to peer rv rental site very similar to both of the other rv rental sites the difference is that are commission based 20% and above per rental and we will be one flat monthly rate and they keep all the earnings. Below is photo that will help you with the color scheme and the look and feel of the design

```html
<!DOCTYPE html>
<html lang="en">
<head>
<meta charset="utf-8">
<title>Zandoprik.com — Peer-to-Peer RV Rental</title>
<link href="https://fonts.googleapis.com/css2?family=Inter:wght@400;500;600;700&family=Source+Serif+4:wght@500;600&display=swap" rel="stylesheet">
<style>
:root{
  --forest:#1b2417;
  --panel:#263022;
  --olive:#6f8a3a;
  --olive-btn:#7a9447;
  --olive-light:#8fae4e;
  --cream:#f5f2eb;
  --ink:#1f261b;
  --muted:#5d6258;
  --line:rgba(255,255,255,.14);
  --white:#ffffff;
}
*{box-sizing:border-box;margin:0;padding:0}
html,body{width:1200px;height:2249px;overflow:hidden}
body{font-family:"Inter",sans-serif;color:var(--ink);background:var(--cream);position:relative}
svg{display:block}

/* hero */
.hero{position:absolute;left:0;top:0;width:1200px;height:776px;background:var(--forest);overflow:hidden;color:var(--white)}
.hero-photo{position:absolute;inset:0;background:
  radial-gradient(ellipse 520px 340px at 830px 250px,rgba(196,150,82,.55),transparent 70%),
  radial-gradient(ellipse 300px 200px at 870px 340px,rgba(220,215,200,.35),transparent 70%),
  linear-gradient(90deg,#182014 0%,#1d2618 38%,#3a3a26 62%,#2a2c1d 85%,#182014 100%)}
.nav{position:absolute;top:26px;left:58px;right:58px;height:48px;display:flex;align-items:center}
.logo{font-family:"Source Serif 4",serif;font-weight:600;font-size:30px;color:var(--white);letter-spacing:-.5px}
.nav-links{display:flex;gap:42px;margin-left:138px;font-size:14px;font-weight:500}
.btn-signup{margin-left:auto;background:var(--olive-btn);color:var(--white);font-size:14px;font-weight:600;padding:14px 26px;border-radius:14px}
.eyebrow{font-size:13px;font-weight:600;letter-spacing:.6px;text-transform:uppercase;color:var(--olive-light)}
.hero .eyebrow{position:absolute;left:66px;top:152px;color:#9bb65c}
.hero h1{position:absolute;left:64px;top:180px;font-family:"Source Serif 4",serif;font-weight:600;font-size:62px;line-height:70px}
.hero h1 span{color:#8aa64a}
.hero-sub{position:absolute;left:66px;top:346px;font-size:17px;line-height:31px}
.search{position:absolute;left:63px;top:440px;width:1050px;height:180px}
.tabs{position:relative;z-index:1;display:flex;width:390px;height:60px;padding-left:26px;font-size:14px;font-weight:600;background:rgba(34,43,30,.92);border-radius:14px 14px 0 0}
.tab{padding:22px 0 0;width:163px;text-align:center}
.tab.active{border-bottom:3px solid var(--olive-light)}
.fields{position:absolute;top:52px;left:0;right:0;height:128px;background:rgba(34,43,30,.92);border-radius:0 14px 14px 14px;display:flex;align-items:flex-start;padding:34px 26px 0;gap:22px}
.field label{display:block;font-size:13px;font-weight:500;margin-bottom:9px}
.input{height:47px;border:1px solid rgba(255,255,255,.22);border-radius:6px;display:flex;align-items:center;gap:8px;padding:0 14px;font-size:13px;color:#cfd2c8;justify-content:space-between}
.f-loc .input{width:214px;justify-content:flex-start}
.f-date .input{width:192px}
.f-guest .input{width:151px;color:var(--white)}
.btn-search{margin-top:28px;width:155px;height:48px;border-radius:8px;background:var(--olive-btn);color:var(--white);font-weight:600;font-size:14px;display:flex;align-items:center;justify-content:center}
.perks{position:absolute;left:63px;top:668px;width:1050px;display:flex}
.perk{display:flex;gap:18px;align-items:flex-start;padding:10px 18px;border-right:1px solid var(--line)}
.perk:last-child{border-right:none}
.perk h3{font-size:13.5px;font-weight:600;margin-bottom:6px;white-space:nowrap}
.perk p{font-size:12px;line-height:22px;color:#d8dbd0;white-space:nowrap}
.perk-first{align-items:center}

/* lifestyle */
.lifestyle-photo{position:absolute;left:63px;top:826px;width:499px;height:314px;border-radius:14px;background:
  radial-gradient(circle at 200px 250px,rgba(240,150,60,.6),transparent 90px),
  radial-gradient(ellipse at 360px 150px,rgba(220,160,90,.45),transparent 160px),
  linear-gradient(180deg,#3e4a58 0%,#2a3530 45%,#1c2219 100%)}
.years{position:absolute;left:436px;top:1028px;width:114px;height:130px;border-radius:12px;background:var(--olive);color:var(--white);padding:22px 18px}
.years b{font-family:"Source Serif 4",serif;font-weight:500;font-size:34px;display:block;margin-bottom:6px}
.years span{font-size:13px;line-height:24px}
.lifestyle-text{position:absolute;left:630px;top:848px}
.lifestyle-text .eyebrow{color:var(--olive)}
.lifestyle-text h2{font-family:"Source Serif 4",serif;font-weight:600;font-size:40px;line-height:45px;margin-top:10px}
.lifestyle-text p{font-size:15px;line-height:27px;color:#3d4438;margin-top:18px;width:340px}
.btn{display:inline-flex;align-items:center;justify-content:center;background:var(--olive);color:var(--white);font-weight:600;font-size:14px;border-radius:24px}
.lifestyle-text .btn{margin-top:20px;width:130px;height:48px}

/* picks */
.picks-head{position:absolute;left:63px;top:1194px;right:73px}
.picks-head .eyebrow{color:var(--olive)}
.picks-head h2{font-family:"Source Serif 4",serif;font-weight:600;font-size:32px;margin-top:8px}
.view-all{position:absolute;right:0;top:32px;font-size:14px;font-weight:600;color:var(--olive);display:flex;gap:10px;align-items:center}
.cards{position:absolute;left:63px;top:1276px;display:flex;gap:20px}
.card{width:253px;height:302px;background:var(--white);border-radius:10px;overflow:hidden;box-shadow:0 2px 10px rgba(0,0,0,.06);position:relative}
.card-photo{height:170px}
.heart{position:absolute;right:12px;top:14px}
.card-body{padding:14px 15px}
.card h3{font-size:13.5px;font-weight:500}
.loc{font-size:10px;color:#9a9e94;display:flex;align-items:center;gap:4px;margin-top:7px}
.specs{display:flex;gap:22px;font-size:12.5px;margin-top:12px}
.specs span{display:flex;gap:6px;align-items:center}
.price-row{display:flex;justify-content:space-between;margin-top:18px;font-size:14px}
.price-row b{font-weight:700}
.price-row small{font-size:13px;color:var(--muted)}
.rating{font-size:13px;color:var(--muted);display:flex;gap:5px;align-items:center}

/* how */
.how{position:absolute;left:0;top:1610px;width:1200px;height:263px;background:var(--forest);color:var(--white);text-align:center}
.how .eyebrow{margin-top:28px;font-size:12px}
.how h2{font-family:"Source Serif 4",serif;font-weight:500;font-size:28px;margin-top:8px}
.steps{position:absolute;top:108px;left:170px;display:flex;text-align:left}
.step{display:flex;gap:22px;align-items:center;width:322px;position:relative}
.step-arrow{position:absolute;left:268px;top:46px}
.ring{width:100px;height:100px;border-radius:50%;border:2px solid var(--olive-light);display:flex;align-items:center;justify-content:center;flex:none}
.step h4{font-size:13.5px;font-weight:600;display:flex;align-items:center;gap:8px}
.num{width:22px;height:22px;border-radius:50%;background:var(--olive-light);font-size:12px;display:flex;align-items:center;justify-content:center}
.step p{font-size:12.5px;line-height:22px;margin-top:8px;color:#dfe2d8}

/* newsletter */
.news{position:absolute;left:168px;top:1900px;width:862px;display:flex;align-items:center}
.mail{width:74px;height:74px;border-radius:20px;background:var(--olive);display:flex;align-items:center;justify-content:center}
.news-text{margin-left:28px;width:320px}
.news-text h3{font-family:"Source Serif 4",serif;font-weight:600;font-size:21px;line-height:27px}
.news-text p{font-size:12.5px;line-height:21px;color:var(--muted);margin-top:6px}
.subscribe{margin-left:auto;display:flex}
.subscribe .email{width:272px;height:49px;border:1px solid #ddd;border-right:none;border-radius:8px 0 0 8px;background:var(--white);font-size:13px;color:#9a9e94;display:flex;align-items:center;padding-left:26px}
.subscribe .go{width:168px;height:49px;background:var(--olive);color:var(--white);border-radius:0 8px 8px 0;font-weight:600;font-size:14px;display:flex;align-items:center;justify-content:center}

/* footer */
.footer{position:absolute;left:0;top:2030px;width:1200px;height:219px;background:var(--forest);color:var(--white)}
.footer .logo{position:absolute;left:66px;top:30px;font-size:26px}
.footer .blurb{position:absolute;left:66px;top:76px;font-size:12px;line-height:22px;width:212px;color:#e3e6dc}
.social{position:absolute;left:66px;top:152px;display:flex;gap:18px}
.social i{width:22px;height:22px;border-radius:50%;background:var(--white);display:block}
.fcol{position:absolute;top:36px;font-size:12px;line-height:22.5px;color:#e3e6dc}
.fcol h5{font-size:12px;font-weight:600;color:var(--white);margin-bottom:10px;letter-spacing:.3px}
.badge{width:125px;height:38px;border-radius:7px;background:#000;border:1px solid #555;margin-bottom:16px}
.copy{position:absolute;left:0;right:0;bottom:12px;text-align:center;font-size:12px;color:#cfd2c8}
</style>
</head>
<body>

<header class="hero">
  <div class="hero-photo" role="img" aria-label="Motorhome driving along a winding mountain road through pine forest at sunset"></div>
  <nav class="nav">
    <div class="logo">Zandoprik.com</div>
    <div class="nav-links"><span>How It Works</span><span>List Your RV</span><span>Browse RVs</span><span>About Us</span><span>FAQs</span></div>
    <div class="btn-signup">Sign Up</div>
  </nav>
  <p class="eyebrow">Peer-to-Peer RV Rental</p>
  <h1>Rent. Explore.<br><span>Make Memories.</span></h1>
  <p class="hero-sub">The easiest way to rent an RV from real people.<br>List it. Rent it. Bank it.</p>

  <form class="search">
    <div class="tabs"><div class="tab active">Find an RV</div><div class="tab">List Your RV</div></div>
    <div class="fields">
      <div class="field f-loc"><label>Pickup Location</label>
        <div class="input"><svg width="12" height="14" viewBox="0 0 12 14"><path d="M6 13s4.5-4.3 4.5-7.5a4.5 4.5 0 0 0-9 0C1.5 8.7 6 13 6 13z" fill="none" stroke="#cfd2c8" stroke-width="1.2"/><circle cx="6" cy="5.5" r="1.6" fill="none" stroke="#cfd2c8" stroke-width="1.2"/></svg>Enter location</div></div>
      <div class="field f-date"><label>Pickup Date</label>
        <div class="input">Select date<svg width="14" height="14" viewBox="0 0 14 14"><rect x="1" y="2" width="12" height="11" rx="1.5" fill="none" stroke="#cfd2c8" stroke-width="1.2"/><path d="M1 5.5h12M4 1v2.5M10 1v2.5M4 8h2M8 8h2M4 10.5h2" stroke="#cfd2c8" stroke-width="1.2"/></svg></div></div>
      <div class="field f-date"><label>Return Date</label>
        <div class="input">Select date<svg width="14" height="14" viewBox="0 0 14 14"><rect x="1" y="2" width="12" height="11" rx="1.5" fill="none" stroke="#cfd2c8" stroke-width="1.2"/><path d="M1 5.5h12M4 1v2.5M10 1v2.5M4 8h2M8 8h2M4 10.5h2" stroke="#cfd2c8" stroke-width="1.2"/></svg></div></div>
      <div class="field f-guest"><label>Guests</label>
        <div class="input">Any<svg width="12" height="8" viewBox="0 0 12 8"><path d="M1.5 1.5 6 6l4.5-4.5" fill="none" stroke="#fff" stroke-width="1.6"/></svg></div></div>
      <div class="btn-search">Search</div>
    </div>
  </form>

  <section class="perks">
    <div class="perk perk-first" style="width:275px"><svg width="36" height="32" viewBox="0 0 36 32" fill="none" stroke="#8fae4e" stroke-width="1.6"><circle cx="18" cy="9" r="5"/><circle cx="7" cy="12" r="3.5"/><circle cx="29" cy="12" r="3.5"/><path d="M9 28c0-6 4-10 9-10s9 4 9 10zM1 26c0-4 2.5-7 6-7M35 26c0-4-2.5-7-6-7"/></svg>
      <div><h3>Peer-to-Peer</h3><p style="font-size:11.5px">Real people, real experiences</p></div></div>
    <div class="perk" style="width:254px"><svg width="36" height="36" viewBox="0 0 36 36" fill="none" stroke="#8fae4e" stroke-width="1.6"><circle cx="18" cy="18" r="16"/><path d="M12 24 24 12"/><circle cx="13" cy="13" r="2.2"/><circle cx="23" cy="23" r="2.2"/></svg>
      <div><h3>20%+ Commission</h3><p>Earn more with<br>every booking</p></div></div>
    <div class="perk" style="width:276px"><svg width="40" height="34" viewBox="0 0 40 34" fill="none" stroke="#8fae4e" stroke-width="1.6"><rect x="2" y="7" width="34" height="25" rx="3"/><path d="M6 7 28 2l2 5"/><path d="M26 15h12v9H26a4.5 4.5 0 0 1 0-9z"/><circle cx="28" cy="19.5" r="1.2"/></svg>
      <div><h3>One Flat Monthly Rate</h3><p>Keep all your earnings<br>with no hidden fees</p></div></div>
    <div class="perk" style="width:245px"><svg width="34" height="38" viewBox="0 0 34 38" fill="none" stroke="#8fae4e" stroke-width="1.6"><path d="M17 2 31 7v11c0 9-6 15-14 18C9 33 3 27 3 18V7z"/><path d="m11 19 4.5 4.5L24 14"/></svg>
      <div><h3>Secure &amp; Insured</h3><p>Rent with confidence<br>and peace of mind</p></div></div>
  </section>
</header>

<section class="lifestyle">
  <div class="lifestyle-photo" role="img" aria-label="Friends gathered around a campfire beside a parked RV by a mountain lake at dusk"></div>
  <div class="years"><b>25+</b><span>Years of<br>Adventure</span></div>
  <div class="lifestyle-text" style="top:820px">
    <p class="eyebrow">The RV Lifestyle</p>
    <h2>Where Roads<br>Lead to Memories.</h2>
    <p>From weekend getaways to cross-country adventures — find the perfect RV and experience the freedom of the open road.</p>
    <a class="btn">Explore RVs</a>
  </div>
</section>

<section class="picks">
  <div class="picks-head">
    <p class="eyebrow">Popular RVs</p>
    <h2>Top Picks for Your Next Adventure</h2>
    <span class="view-all">View all RVs <svg width="14" height="12" viewBox="0 0 14 12"><path d="M1 6h11M8 2l4 4-4 4" fill="none" stroke="#6f8a3a" stroke-width="1.6"/></svg></span>
  </div>
  <div class="cards">
    <article class="card">
      <div class="card-photo" role="img" aria-label="Class C motorhome parked in a pine forest below snowy peaks" style="background:linear-gradient(180deg,#8fa6b8,#52613e 55%,#3a4430)"></div>
      <svg class="heart" width="16" height="15" viewBox="0 0 16 15"><path d="M8 13.5S1.5 9.5 1.5 5a3.3 3.3 0 0 1 6.5-1 3.3 3.3 0 0 1 6.5 1c0 4.5-6.5 8.5-6.5 8.5z" fill="none" stroke="#fff" stroke-width="1.5"/></svg>
      <div class="card-body"><h3>2022 Wayfarro Tamsen</h3>
        <p class="loc"><svg width="8" height="10" viewBox="0 0 12 14"><path d="M6 13s4.5-4.3 4.5-7.5a4.5 4.5 0 0 0-9 0C1.5 8.7 6 13 6 13z" fill="none" stroke="#6f8a3a" stroke-width="1.6"/></svg>Denver, CO</p>
        <div class="specs"><span><svg width="14" height="12" viewBox="0 0 14 12" fill="none" stroke="#555" stroke-width="1.2"><path d="M1 11V6h12v5M1 9h12M3 6V2h8v4"/></svg>Sleeps 4</span><span><svg width="14" height="12" viewBox="0 0 14 12" fill="none" stroke="#555" stroke-width="1.2"><path d="M1 11V6h12v5M1 9h12M3 6V2h8v4"/></svg><b>24</b> ft</span></div>
        <div class="price-row"><span><b>$175</b> <small>/night</small></span><span class="rating"><svg width="12" height="12" viewBox="0 0 12 12"><path d="m6 .5 1.7 3.6 3.8.4-2.9 2.6.9 3.8L6 9 2.5 10.9l.9-3.8L.5 4.5l3.8-.4z" fill="#e09a2c"/></svg>4.9 (28)</span></div>
      </div>
    </article>
    <article class="card">
      <div class="card-photo" role="img" aria-label="Travel trailer beside a lake with mountains behind" style="background:linear-gradient(180deg,#aab8c6,#7c8a8a 45%,#3c4a3a)"></div>
      <svg class="heart" width="16" height="15" viewBox="0 0 16 15"><path d="M8 13.5S1.5 9.5 1.5 5a3.3 3.3 0 0 1 6.5-1 3.3 3.3 0 0 1 6.5 1c0 4.5-6.5 8.5-6.5 8.5z" fill="none" stroke="#fff" stroke-width="1.5"/></svg>
      <div class="card-body"><h3>2021 Kestrel Ossary</h3>
        <p class="loc"><svg width="8" height="10" viewBox="0 0 12 14"><path d="M6 13s4.5-4.3 4.5-7.5a4.5 4.5 0 0 0-9 0C1.5 8.7 6 13 6 13z" fill="none" stroke="#6f8a3a" stroke-width="1.6"/></svg>Boise, ID</p>
        <div class="specs"><span><svg width="14" height="12" viewBox="0 0 14 12" fill="none" stroke="#555" stroke-width="1.2"><path d="M1 11V6h12v5M1 9h12M3 6V2h8v4"/></svg>Sleeps 6</span><span><svg width="14" height="12" viewBox="0 0 14 12" fill="none" stroke="#555" stroke-width="1.2"><path d="M1 11V6h12v5M1 9h12M3 6V2h8v4"/></svg><b>29</b> ft</span></div>
        <div class="price-row"><span><b>$129</b> <small>/night</small></span><span class="rating"><svg width="12" height="12" viewBox="0 0 12 12"><path d="m6 .5 1.7 3.6 3.8.4-2.9 2.6.9 3.8L6 9 2.5 10.9l.9-3.8L.5 4.5l3.8-.4z" fill="#e09a2c"/></svg>4.8 (19)</span></div>
      </div>
    </article>
    <article class="card">
      <div class="card-photo" role="img" aria-label="Fifth-wheel trailer in a forest clearing at sunset" style="background:linear-gradient(180deg,#d89a5a,#7a5a3a 45%,#2e2a20)"></div>
      <svg class="heart" width="16" height="15" viewBox="0 0 16 15"><path d="M8 13.5S1.5 9.5 1.5 5a3.3 3.3 0 0 1 6.5-1 3.3 3.3 0 0 1 6.5 1c0 4.5-6.5 8.5-6.5 8.5z" fill="none" stroke="#fff" stroke-width="1.5"/></svg>
      <div class="card-body"><h3>2023 Halvern Lumora</h3>
        <p class="loc"><svg width="8" height="10" viewBox="0 0 12 14"><path d="M6 13s4.5-4.3 4.5-7.5a4.5 4.5 0 0 0-9 0C1.5 8.7 6 13 6 13z" fill="none" stroke="#6f8a3a" stroke-width="1.6"/></svg>Portland, OR</p>
        <div class="specs"><span><svg width="14" height="12" viewBox="0 0 14 12" fill="none" stroke="#555" stroke-width="1.2"><path d="M1 11V6h12v5M1 9h12M3 6V2h8v4"/></svg>Sleeps 8</span><span><svg width="14" height="12" viewBox="0 0 14 12" fill="none" stroke="#555" stroke-width="1.2"><path d="M1 11V6h12v5M1 9h12M3 6V2h8v4"/></svg><b>32</b> ft</span></div>
        <div class="price-row"><span><b>$149</b> <small>/night</small></span><span class="rating"><svg width="12" height="12" viewBox="0 0 12 12"><path d="m6 .5 1.7 3.6 3.8.4-2.9 2.6.9 3.8L6 9 2.5 10.9l.9-3.8L.5 4.5l3.8-.4z" fill="#e09a2c"/></svg>5.0 (35)</span></div>
      </div>
    </article>
    <article class="card">
      <div class="card-photo" role="img" aria-label="Class C motorhome on a coastal road with green hills" style="background:linear-gradient(180deg,#b9c8d2,#7d9288 45%,#4a5a44)"></div>
      <svg class="heart" width="16" height="15" viewBox="0 0 16 15"><path d="M8 13.5S1.5 9.5 1.5 5a3.3 3.3 0 0 1 6.5-1 3.3 3.3 0 0 1 6.5 1c0 4.5-6.5 8.5-6.5 8.5z" fill="none" stroke="#fff" stroke-width="1.5"/></svg>
      <div class="card-body"><h3>2019 Bramble Corvane</h3>
        <p class="loc"><svg width="8" height="10" viewBox="0 0 12 14"><path d="M6 13s4.5-4.3 4.5-7.5a4.5 4.5 0 0 0-9 0C1.5 8.7 6 13 6 13z" fill="none" stroke="#6f8a3a" stroke-width="1.6"/></svg>San Diego, CA</p>
        <div class="specs"><span><svg width="14" height="12" viewBox="0 0 14 12" fill="none" stroke="#555" stroke-width="1.2"><path d="M1 11V6h12v5M1 9h12M3 6V2h8v4"/></svg>Sleeps 6</span><span><svg width="14" height="12" viewBox="0 0 14 12" fill="none" stroke="#555" stroke-width="1.2"><path d="M1 11V6h12v5M1 9h12M3 6V2h8v4"/></svg><b>26</b> ft</span></div>
        <div class="price-row"><span><b>$160</b> <small>/night</small></span><span class="rating"><svg width="12" height="12" viewBox="0 0 12 12"><path d="m6 .5 1.7 3.6 3.8.4-2.9 2.6.9 3.8L6 9 2.5 10.9l.9-3.8L.5 4.5l3.8-.4z" fill="#e09a2c"/></svg>4.7 (22)</span></div>
      </div>
    </article>
  </div>
</section>

<section class="how">
  <p class="eyebrow">How It Works</p>
  <h2>Renting Made Simple</h2>
  <div class="steps">
    <div class="step"><div class="ring"><svg width="58" height="46" viewBox="0 0 58 46" fill="none" stroke="#fff" stroke-width="2.4"><rect x="2" y="6" width="36" height="24" rx="3"/><path d="M38 14h8l6 8v8H38M8 14h10v8H8zM24 14h8"/><circle cx="12" cy="33" r="4"/><circle cx="44" cy="34" r="9"/><path d="m50 41 6 5"/></svg></div>
      <div><h4><span class="num">1</span>Find Your RV</h4><p>Search local RVs that fit<br>your trip and budget.</p></div>
      <svg class="step-arrow" width="34" height="8" viewBox="0 0 34 8"><path d="M0 4h32M28 1l4 3-4 3" fill="none" stroke="#56683a" stroke-width="1.2"/></svg></div>
    <div class="step"><div class="ring"><svg width="50" height="50" viewBox="0 0 50 50" fill="none" stroke="#fff" stroke-width="2.4"><rect x="3" y="6" width="38" height="36" rx="3"/><path d="M3 15h38M12 2v8M32 2v8"/><path d="M11 22h3M19 22h3M27 22h3M11 30h3M19 30h3" stroke-width="3"/><circle cx="38" cy="38" r="9" fill="#1b2417"/><path d="m34 38 3 3 5-6"/></svg></div>
      <div><h4><span class="num">2</span>Book &amp; Connect</h4><p>Book securely and connect<br>with the RV owner.</p></div>
      <svg class="step-arrow" width="34" height="8" viewBox="0 0 34 8" style="left:282px"><path d="M0 4h32M28 1l4 3-4 3" fill="none" stroke="#56683a" stroke-width="1.2"/></svg></div>
    <div class="step"><div class="ring"><svg width="54" height="52" viewBox="0 0 54 52" fill="none" stroke="#fff" stroke-width="2.4"><path d="M2 30 18 8l8 10 8-8 18 20"/><path d="M14 13l4 4 4-3"/><path d="M28 30c-10 4 6 8-2 14" stroke-width="4"/><path d="M6 30c8 0 8 4 2 8M46 30c-6 0-6 6 0 10"/></svg></div>
      <div><h4><span class="num">3</span>Hit the Road</h4><p>Pick up, enjoy your trip,<br>and make memories!</p></div></div>
  </div>
</section>

<section class="news">
  <div class="mail"><svg width="34" height="26" viewBox="0 0 34 26" fill="none" stroke="#fff" stroke-width="2"><rect x="1" y="1" width="32" height="24" rx="2"/><path d="m1 3 16 12L33 3M1 24l12-11M33 24 21 13"/></svg></div>
  <div class="news-text"><h3>Adventure Awaits.<br>Let's Go!</h3><p>Sign up for travel tips, exclusive deals,<br>and RV inspiration.</p></div>
  <div class="subscribe"><div class="email">Enter your email</div><div class="go">Subscribe</div></div>
</section>

<footer class="footer">
  <div class="logo">Zandoprik.com</div>
  <p class="blurb">The peer-to-peer RV rental marketplace that helps you earn more and travel further.</p>
  <div class="social"><i></i><i></i><i></i></div>
  <div class="fcol" style="left:397px"><h5>COMPANY</h5>About Us<br>How It Works<br>List Your RV<br>Browse RVs<br>Blog</div>
  <div class="fcol" style="left:555px"><h5>SUPPORT</h5>FAQ<br>Safety<br>Insurance<br>Contact Us</div>
  <div class="fcol" style="left:705px"><h5>LEGAL</h5>Terms of Service<br>Privacy Policy</div>
  <div class="fcol" style="left:947px"><h5>DOWNLOAD THE APP</h5><div class="badge"></div><div class="badge"></div></div>
  <p class="copy">© 2025 Zandoprik.com. All rights reserved.</p>
</footer>

</body>
</html>
```